Football (soccer) board game app design

Hi,

We are a start up looking for a gameplay design for an app. It is a football trivia app that consists of four main screens; login/register, main navigation, gameplay, question.

OVERALL:
We want our app to be kept in a dark theme. Black or very dark gray is preferable, with a couple of nice colors to give it a stylish touch. We like flat designs, but are open for ideas within the general structure design. The logo can be used in the app, but feel free to improve it you feel you can. In the attached material we have tried to outline some of our ideas and other designs friends have helped us make.

LOGIN/REGISTER:
We want a simple login. Email, password, Chatterly login and the possibility to register a new user. Live search check whether the email is valid and free, and there is also live validation of passwords. If this could be incorporated in the design it would be nice.

MAIN NAVIGATION:
In the main navigation screen we want it to be divided into tabs. A home, my games, my categories and a ranking tab. In the top bar it should be possible to search for categories as well as there should be a button to go to settings.

The Home tab
In the home tab we want a "Quick Play" button, and a list of featured categories. A category can be unlocked or locked, which should be illustrated somehow. When a category is tapped it should divide the block into a left and right tap area, where the user can choose to "Beat to unlock" or "Buy to unlock" if locked and "Practice" or "Challenge Friend" if already unlocked.

The My Games tab
In the my games tab, the current games should be divided into three lists. First "your turn", then "opponents turn" and finally "finished games".

The My Categories tab
This tab should include a list of categories, which the user have bought, but as of design it is fairly similar to the blocks in home tab. So not much different here.

The Ranking tab
Ranking should show a set of leaderboards; Today, This Week, This Month, etc. The row in a leaderboard should have teamname and a win percentage.

GAMEPLAY:
The gameplay is inspired by an old football (soccer) board game from the 1950's, and our gameplay consists of three core elements; a football (soccer) pitch, 11 players and a scoreboard.

The football (soccer) pitch
What we need is a pitch seen from behind the goal line. The important issue here, is the perspective, as we want 11 players on the field formed as a 4-3-3 formation, being 1 goalkeeper, 4 defenders, 3 midfielder and 3 strikers. They should all be touchable without overlap. In the other end we want a goal that should be touchable as well. The goal in the nearest end do not have to be visible. Due to the perspective of the field and the fact that players and goal should be touchable, of course give you the opportunity to play around with the proportions of both players and goal. We rather want a large goal being out of proportions, than a small goal with a tiny tap area. Around the field (sidelines and beside the goal) we would like advertising banners like seen on a real stadium.

The players
As mentioned we want 11 players in a 4-3-3 formation. The players should be attached to the board with springs as seen on some of the very old board games, where you could flick the player to pass the ball. This also means that we want the players to be placed in an indentation for the ball to fall into and it would be very cool if you could illustrate the player with the ball, as being pulled back to one of the sides, just enough to see the ball at his feet. The players should be large enough for a user to tap them, hence it would also be beneficial if they are not overlapping. For a start we would like to see the players in a blue shirt and white shorts (socks are not necessary as they are placed on a spring).

Scoreboard
On the scoreboard above the field, we need information such as the names of the two teams (could be FC Brightmoor and Tall Oak Rovers), the score (2-1), minutes played (42), and which half (1st). We also want a progress bar that illustrates how many moves you have used ranging from 0-5. The scoreboard could be inspired from the ones seen around stadiums across the world, but feel free to improvise.

What We Are Looking for
We are looking for full PSD and AI files so we can use them to make minor changes like colors on shirts and shorts, colors on pitch, etc. We really want you to be innovative and inspire us, as we are not designers ourselves. In the attached files, we have tried to sketch out a design that covers our initial ideas. We are looking for a professional look, and having the players and field look like a real board game would just be awesome. A combination of the look from the realistic pitch with advertising banners around it, the idea of our spring-players and the initial thoughts of a design illustrated in our sketch, should help you along. Flat design, cartoonish or somewhere in between is up to you, we just want you to impress and make "wow"-feeling.

QUESTION:
The final screen should display a question with four possible answers. There should be a green/checkmark when correct answer, and a red/cross if incorrect.

That's all. We are looking very much forward to see your designs!
Updates

Hi all,

We have changed the terms of the contest to now have a guaranteed payment, and we are really looking forward to see your designs! Good luck.

/ Mikkel and Anders

By request we have now uploaded an AI-file with the logo for you to play around with. We are looking forward to see your designs.

/ Mikkel and Anders

Reason: Hi designers, We are really happy with the progress being made, and are looking forward to see some of the designs that are still work in progress. However the amount of designs received, has not reached our expectations yet. Therefore we are extending the deadline for seven more days, so designers, that are still working on their designs can continue their work without a stressing deadline in the horizon. Good luck to all of you. We are looking very much forward to see, what you are able to produce. Best regards, Mikkel and Anders

Reason: Hi all, We still have a lot of designers in the competition , who are battling to finish their designs, therefore we have decided to extend the deadline once more. Good luck to all of you!

Target Market(s)

Football (soccer) fans

Industry/Entity Type

Advertising

```html
<!DOCTYPE html>
<html lang="en">
<head>
<meta charset="utf-8">
<title>Football Trivia – Home</title>
<link rel="stylesheet" href="https://fonts.googleapis.com/css2?family=Lato:wght@300;400;700&display=swap">
<style>
  :root {
    --page-bg: #f1f1f1;
    --status-bg: #1d1d1d;
    --topbar-bg: #232323;
    --pill-bg: #333333;
    --tabs-bg: #575757;
    --tabs-rule: #9a9a9a;
    --choose-bg: #393939;
    --quick-bg: #454545;
    --action-bg: #1c1c1c;
    --text: #ffffff;
    --text-soft: #e4e4e4;
    --text-muted: #bdbdbd;
    --beat-red: #e0302b;
    --buy-green: #4f9a25;
  }
  * { box-sizing: border-box; margin: 0; padding: 0; }
  html, body {
    width: 1200px; height: 1000px; overflow: hidden;
    background: var(--page-bg);
    font-family: "Lato", "Helvetica Neue", Arial, sans-serif;
  }
  .screen {
    position: absolute; left: 338px; top: 37px;
    width: 388px; height: 686px;
    transform: scale(1.35); transform-origin: top left;
    background: #111; overflow: hidden; color: var(--text);
    box-shadow: 0 10px 30px rgba(0,0,0,.25);
  }
  .status-bar {
    height: 24px; background: var(--status-bg);
    display: flex; align-items: center; justify-content: space-between;
    padding: 0 8px; font-size: 13px; font-weight: 700;
  }
  .status-left { display: flex; align-items: center; gap: 4px; width: 80px; }
  .signal { display: flex; gap: 2px; }
  .signal i { width: 6px; height: 6px; border-radius: 50%; background: #fff; display: block; }
  .battery { width: 80px; display: flex; justify-content: flex-end; }
  .battery span { width: 26px; height: 11px; border: 1px solid #fff; border-radius: 2px; padding: 1px; display: block; }
  .battery span::after { content: ""; display: block; width: 100%; height: 100%; background: #fff; }

  .top-bar {
    height: 54px; background: var(--topbar-bg); position: relative;
    display: flex; align-items: center; justify-content: center;
  }
  .settings-btn { position: absolute; left: 13px; top: 12px; }
  .top-title { font-size: 20px; font-weight: 400; }
  .wins-pill {
    position: absolute; right: 4px; top: 9px; height: 34px;
    padding: 0 12px; border-radius: 17px; background: var(--pill-bg);
    font-size: 11.5px; color: var(--text-muted);
    display: flex; align-items: center;
  }

  .tabs {
    height: 54px; background: var(--tabs-bg); position: relative;
    display: flex; align-items: center; justify-content: space-around;
    border-bottom: 3px solid var(--tabs-rule); font-size: 14px;
  }
  .tab { color: var(--text-soft); font-weight: 300; }
  .tab.is-active { font-weight: 700; color: #fff; position: relative; }
  .tab.is-active::after {
    content: ""; position: absolute; left: 50%; bottom: -15px; margin-left: -5px;
    border: 5px solid transparent; border-bottom-color: var(--tabs-rule); border-top: 0;
  }

  .choose-row {
    height: 53px; background: var(--choose-bg);
    display: flex; align-items: center; justify-content: center;
    font-size: 19.5px; font-weight: 300; color: var(--text-soft);
  }
  .quick-play {
    height: 69px; background: var(--quick-bg);
    display: flex; align-items: center; justify-content: center;
    font-size: 19.5px; font-weight: 300; letter-spacing: .3px;
  }

  .category {
    position: relative; height: 115px; overflow: hidden;
  }
  .category-photo { position: absolute; inset: 0; }
  .photo-stadium {
    background: linear-gradient(180deg, #5a6c86 0%, #26303e 28%, #1d2430 42%, #3f6a2c 55%, #4f8a2e 75%, #3e7424 100%);
  }
  .photo-blurred {
    background: radial-gradient(ellipse at 40% 40%, #8a7764 0%, #5e4d3e 45%, #3a2f26 100%);
  }
  .photo-ceremony {
    background: linear-gradient(180deg, #3b5a33 0%, #9a9e98 35%, #c9ccc8 55%, #4d7a35 80%, #3d6a28 100%);
  }
  .photo-crowd {
    background: linear-gradient(180deg, #c9d6e3 0%, #5f7ea6 60%, #32486a 100%);
  }
  .category-caption {
    position: absolute; left: 13px; bottom: 12px;
    font-size: 16.5px; font-weight: 300; color: #fff;
    text-shadow: 0 1px 2px rgba(0,0,0,.4);
  }
  .category-caption small { font-size: 13.5px; }
  .category-arrow { position: absolute; right: 12px; bottom: 9px; }
  .lock-badge {
    position: absolute; left: 170px; top: 20px;
    width: 46px; height: 46px; border-radius: 50%;
    background: #eeeeee; display: flex; align-items: center; justify-content: center;
  }

  .unlock-actions {
    position: relative; height: 51px; background: var(--action-bg);
    display: flex; align-items: center; justify-content: center; gap: 20px;
    font-size: 11.5px; color: #fff;
  }
  .unlock-actions::before {
    content: ""; position: absolute; left: 186px; top: -6px;
    border: 6px solid transparent; border-bottom-color: var(--action-bg); border-top: 0;
  }
  .unlock-option { display: flex; align-items: center; gap: 7px; }
  .unlock-icon {
    width: 30px; height: 30px; border-radius: 50%;
    display: flex; align-items: center; justify-content: center;
  }
  .unlock-icon.beat { background: var(--beat-red); }
  .unlock-icon.buy { background: var(--buy-green); }
  .unlock-divider { width: 1px; height: 14px; background: #444; }
  .category.is-peek { height: 36px; }
</style>
</head>
<body>
<main class="screen">
  <div class="status-bar">
    <div class="status-left">
      <div class="signal"><i></i><i></i><i></i><i></i><i></i></div>
      <svg width="16" height="12" viewBox="0 0 16 12" aria-hidden="true"><path d="M8 11 L5.5 8.2 A3.6 3.6 0 0 1 10.5 8.2 Z M2.8 5.6 A7.5 7.5 0 0 1 13.2 5.6" fill="#fff" stroke="#fff" stroke-width="1.6"/><path d="M0.5 3 A11 11 0 0 1 15.5 3" fill="none" stroke="#fff" stroke-width="1.6"/></svg>
    </div>
    <span class="clock">9:00 AM</span>
    <div class="battery"><span></span></div>
  </div>

  <header class="top-bar">
    <svg class="settings-btn" width="30" height="30" viewBox="0 0 30 30" aria-label="Settings">
      <circle cx="15" cy="15" r="13.5" fill="none" stroke="#ddd" stroke-width="1.5"/>
      <g fill="#fff" transform="translate(15 15)">
        <circle r="5.2"/>
        <rect x="-1.6" y="-8" width="3.2" height="16" rx="0.6"/>
        <rect x="-1.6" y="-8" width="3.2" height="16" rx="0.6" transform="rotate(45)"/>
        <rect x="-1.6" y="-8" width="3.2" height="16" rx="0.6" transform="rotate(90)"/>
        <rect x="-1.6" y="-8" width="3.2" height="16" rx="0.6" transform="rotate(135)"/>
      </g>
      <circle cx="15" cy="15" r="2.2" fill="#232323"/>
    </svg>
    <h1 class="top-title">Title</h1>
    <div class="wins-pill">137 won matches</div>
  </header>

  <nav class="tabs">
    <span class="tab is-active">Home</span>
    <span class="tab">My Games</span>
    <span class="tab">My Categories</span>
    <span class="tab">Rankings</span>
  </nav>

  <div class="choose-row">Choose Games Categories</div>
  <div class="quick-play">QUICK PLAY</div>

  <section class="category">
    <div class="category-photo photo-stadium" role="img" aria-label="Photo of a floodlit football stadium with a green pitch"></div>
    <span class="category-caption">Feature Categories</span>
    <svg class="category-arrow" width="24" height="24" viewBox="0 0 24 24" aria-hidden="true"><circle cx="12" cy="12" r="11" fill="none" stroke="#fff" stroke-width="1.2"/><path d="M10 7 L15 12 L10 17" fill="none" stroke="#fff" stroke-width="1.4"/></svg>
  </section>

  <section class="category is-locked">
    <div class="category-photo photo-blurred" role="img" aria-label="Blurred photo of a football match in action"></div>
    <div class="lock-badge">
      <svg width="22" height="24" viewBox="0 0 22 24" aria-label="Locked"><path d="M6 10 V7 A5 5 0 0 1 16 7 V10" fill="none" stroke="#3a2f26" stroke-width="2.4"/><rect x="2" y="10" width="18" height="13" rx="2" fill="#3a2f26"/></svg>
    </div>
    <span class="category-caption">Feature Categories <small>(Locked)</small></span>
    <svg class="category-arrow" width="24" height="24" viewBox="0 0 24 24" aria-hidden="true"><circle cx="12" cy="12" r="11" fill="none" stroke="#fff" stroke-width="1.2"/><path d="M7 10 L12 15 L17 10" fill="none" stroke="#fff" stroke-width="1.4"/></svg>
  </section>

  <div class="unlock-actions">
    <div class="unlock-option">
      <span class="unlock-icon beat">
        <svg width="16" height="18" viewBox="0 0 16 18" aria-hidden="true"><rect x="3" y="7" width="10" height="9" rx="3" fill="#fff"/><rect x="4" y="2" width="2" height="7" rx="1" fill="#fff"/><rect x="7" y="1" width="2" height="7" rx="1" fill="#fff"/><rect x="10" y="2" width="2" height="7" rx="1" fill="#fff"/></svg>
      </span>
      <span>Beat to Unlock</span>
    </div>
    <span class="unlock-divider"></span>
    <div class="unlock-option">
      <span class="unlock-icon buy">
        <svg width="16" height="14" viewBox="0 0 16 14" aria-hidden="true"><path d="M1 1 H3.5 L5.5 9 H13 L14.5 3.5 H4.3" fill="none" stroke="#fff" stroke-width="1.5"/><circle cx="6" cy="12" r="1.3" fill="#fff"/><circle cx="12.5" cy="12" r="1.3" fill="#fff"/></svg>
      </span>
      <span>Buy to Unlock</span>
    </div>
  </div>

  <section class="category">
    <div class="category-photo photo-ceremony" role="img" aria-label="Photo of players holding a large flag in the centre circle of a pitch"></div>
    <span class="category-caption">Feature Categories</span>
    <svg class="category-arrow" width="24" height="24" viewBox="0 0 24 24" aria-hidden="true"><circle cx="12" cy="12" r="11" fill="none" stroke="#fff" stroke-width="1.2"/><path d="M10 7 L15 12 L10 17" fill="none" stroke="#fff" stroke-width="1.4"/></svg>
  </section>

  <section class="category is-peek">
    <div class="category-photo photo-crowd" role="img" aria-label="Photo of a goalmouth scramble in front of a crowd"></div>
  </section>
</main>
</body>
</html>
```